Bright Tooth Dentistry Business Card

We need business cards for our dental office.
We are looking for a clean, elegant design

We provide dental services to children.
Our card needs to be appealing to referring dentists, parents and our team

Target Market(s)

referring dentists, parents and our team

Industry/Entity Type

Dental Clinic

Contact Information for Business Card

4816 Juniper Lane, Suite 100
Cedar Hollow, PA 15237

412-837-2961 Voice
412-837-2962 fax
info@brighttoothdentalpa.com email
www.brighttoothdentalpa.com web

Font styles to use
Sans Serif

Requirements
Must have
• White background - clean, crisp, elegant, simple
• rounded corners
• different color palate - once we come up with design, we will replace the blue with orange, green,
Nice to have
• Follow our logo typeface and colors
• then we can replace color

```html
<!DOCTYPE html>
<html lang="en">
<head>
<meta charset="utf-8">
<title>Bright Tooth Dentistry – Business Card</title>
<link rel="stylesheet" href="https://fonts.googleapis.com/css2?family=Quicksand:wght@600&family=Roboto:wght@500;700&display=swap">
<style>
  :root {
    --brand-blue: #00aeef;
    --brand-grey: #a7a9ac;
    --card-edge: #444444;
    --paper: #ffffff;
  }
  * { margin: 0; padding: 0; box-sizing: border-box; }
  html, body { width: 1200px; height: 1200px; overflow: hidden; background: var(--paper); }
  .sheet { position: relative; width: 1200px; height: 1200px; }
  .card { position: absolute; width: 820px; height: 469px; }
  .card--front { left: 197px; top: 97px; }
  .card--back { left: 191px; top: 641px; }
  .card__art { position: absolute; inset: 0; }
  .brand-name {
    position: absolute; left: 0; right: 0; text-align: center;
    font-family: "Quicksand", sans-serif; font-weight: 600; white-space: nowrap;
  }
  .card--front .brand-name { top: 226px; font-size: 40px; color: var(--brand-blue); }
  .card--back .brand-name { left: 40px; width: 290px; top: 130px; font-size: 25px; color: var(--paper); }
  .web-address {
    position: absolute; left: 0; right: 0; top: 390px; text-align: center;
    font-family: "Roboto", sans-serif; font-weight: 700; font-size: 22px; color: var(--paper);
  }
  .contact {
    position: absolute; right: 58px; top: 266px; text-align: right;
    font-family: "Roboto", sans-serif; font-weight: 700; font-size: 20px; line-height: 1; color: var(--brand-grey);
  }
  .contact__line { position: absolute; right: 0; white-space: nowrap; }
  .contact__line--email { font-weight: 500; }
  .contact__icon { position: absolute; right: -37px; width: 22px; height: 22px; }
</style>
</head>
<body>
<main class="sheet">

  <section class="card card--front">
    <svg class="card__art" viewBox="0 0 820 469" aria-hidden="true">
      <defs><clipPath id="front-clip"><rect x="1" y="1" width="818" height="467" rx="44"/></clipPath></defs>
      <g clip-path="url(#front-clip)">
        <rect width="820" height="469" fill="var(--paper)"/>
        <rect x="116" y="386" width="587" height="42" fill="var(--brand-blue)"/>
        <polygon points="0,383 112,383 131,431 0,431" fill="var(--brand-grey)"/>
        <polygon points="122,383 137,383 156,431 141,431" fill="var(--brand-grey)"/>
        <polygon points="144,383 159,383 178,431 163,431" fill="var(--brand-grey)"/>
        <polygon points="166,383 181,383 200,431 185,431" fill="var(--brand-grey)"/>
        <polygon points="188,383 203,383 222,431 207,431" fill="var(--brand-grey)"/>
        <polygon points="619,383 634,383 615,431 600,431" fill="var(--brand-grey)"/>
        <polygon points="641,383 656,383 637,431 622,431" fill="var(--brand-grey)"/>
        <polygon points="663,383 678,383 659,431 644,431" fill="var(--brand-grey)"/>
        <polygon points="684,383 699,383 680,431 665,431" fill="var(--brand-grey)"/>
        <polygon points="708,383 820,383 820,431 689,431" fill="var(--brand-grey)"/>
      </g>
      <rect x="1" y="1" width="818" height="467" rx="44" fill="none" stroke="var(--card-edge)" stroke-width="1.5"/>
    </svg>
    <p class="brand-name">Bright Tooth Dentistry</p>
    <p class="web-address">www.brighttoothdentalpa.com</p>
  </section>

  <section class="card card--back">
    <svg class="card__art" viewBox="0 0 820 469" aria-hidden="true">
      <defs><clipPath id="back-clip"><rect x="1" y="1" width="818" height="467" rx="44"/></clipPath></defs>
      <g clip-path="url(#back-clip)">
        <rect width="820" height="469" fill="var(--paper)"/>
        <path d="M0,0 H419 L352,170 Q338,203 303,203 H0 Z" fill="var(--brand-grey)"/>
        <path d="M0,0 H409 L344,172 Q330,203 297,203 H0 Z" fill="var(--brand-blue)"/>
        <path d="M647,469 Q660,438 700,438 H820 V469 Z" fill="var(--brand-grey)"/>
        <path d="M656,469 Q670,438 710,438 H820 V469 Z" fill="var(--brand-blue)"/>
      </g>
      <rect x="1" y="1" width="818" height="467" rx="44" fill="none" stroke="var(--card-edge)" stroke-width="1.5"/>
    </svg>
    <p class="brand-name">Bright Tooth Dentistry</p>

    <div class="contact">
      <span class="contact__line" style="top:0">4816 Juniper Lane, Suite 240</span>
      <svg class="contact__icon" style="top:-1px" viewBox="0 0 22 22" aria-hidden="true">
        <circle cx="11" cy="11" r="11" fill="var(--brand-blue)"/>
        <path d="M11 5a4 4 0 0 0-4 4c0 3 4 8 4 8s4-5 4-8a4 4 0 0 0-4-4z" fill="var(--paper)"/>
        <circle cx="11" cy="9" r="1.5" fill="var(--brand-blue)"/>
      </svg>
      <span class="contact__line" style="top:28px">Cedar Hollow, PA 15237</span>
      <span class="contact__line" style="top:66px">412-837-2961</span>
      <svg class="contact__icon" style="top:65px" viewBox="0 0 22 22" aria-hidden="true">
        <circle cx="11" cy="11" r="11" fill="var(--brand-blue)"/>
        <path d="M14.5 13.5l-1.5 1.5c-2.5-1-4.5-3-5.5-5.5L9 8 7.5 5.5 6 7c0 5 4 9 9 9l1.5-1.5z" fill="var(--paper)"/>
      </svg>
      <span class="contact__line" style="top:95px">412-837-2962</span>
      <svg class="contact__icon" style="top:94px" viewBox="0 0 22 22" aria-hidden="true">
        <circle cx="11" cy="11" r="11" fill="var(--brand-blue)"/>
        <rect x="8" y="5" width="6" height="5" fill="var(--paper)"/>
        <rect x="6" y="10" width="10" height="6" rx="1" fill="var(--paper)"/>
      </svg>
      <span class="contact__line contact__line--email" style="top:133px">info@brighttoothdentalpa.com</span>
      <svg class="contact__icon" style="top:132px" viewBox="0 0 22 22" aria-hidden="true">
        <circle cx="11" cy="11" r="11" fill="var(--brand-blue)"/>
        <rect x="6" y="7.5" width="10" height="7" rx="1" fill="var(--paper)"/>
        <path d="M6.5 8l4.5 3.5L15.5 8" fill="none" stroke="var(--brand-blue)" stroke-width="1"/>
      </svg>
    </div>
  </section>

</main>
</body>
</html>
```